Kestrel Capital Circle - Paradigm Shifting Investment Vehicle in Bali*

The presentation is for the Kestrel Capital Circle, a future-thinking and paradigm-shifting leadership collective that is aimed at uniting conscious investors with New Earth projects in Bali, Indonesia. We want to create a presentation pitch deck to investors that encompasses that concept, pairing our royal purple logo with elements of natural green, or white/black that feels organic, purposeful and powerful. Example of our investor deck is attached.

Target Market(s)

High Net Worth Conscious Individuals, Wealthy Nomads looking to move to Bali, community building leaders

Industry/Entity Type

Investment

Logo Text

Kestrel Capital Circle

Font styles to use
Serif
Sans Serif

Colors
6b449b
886aae
b8a6cd
acd037
cadf82
add136
00a990
33b8a4
86cfc6

Requirements
Must have
• Our name of "Kestrel Capital Circle" or "KCC"
Nice to have
• keywords: consciousness, transformational, healing, new paradigm, progress, New Earth, abundance, regenerative, royal, natural, organic, sustainability, future, dream, creation, co-creation
Should not have
• Boring, corporate look

```html
<!DOCTYPE html>
<html lang="en">
<head>
<meta charset="utf-8">
<title>Kestrel Capital Circle – Investment Prospectus</title>
<link href="https://fonts.googleapis.com/css2?family=Playfair+Display+SC:wght@400;700&family=Open+Sans:ital,wght@0,400;0,700;1,400&display=swap" rel="stylesheet">
<style>
:root{
  --plum:#4b2447;
  --plum-soft:rgba(88,38,84,.55);
  --mauve:#b97a6f;
  --forest:#1f5a49;
  --teal:#2aa58e;
  --mint:#86cfc6;
  --pink:#c990c2;
  --magenta:#b0569f;
  --deep-green:#1c4a3c;
  --cream:#f7f6ef;
  --ink:#2d3f39;
  --muted:#a9a9a0;
  --tick:#6f7a74;
}
*{margin:0;padding:0;box-sizing:border-box}
html,body{width:900px;height:1200px;overflow:hidden;background:#fff}
body{position:relative;font-family:"Open Sans",Arial,sans-serif;color:var(--ink)}
.slide{position:absolute;width:313px;height:175px;background:var(--cream);overflow:hidden;box-shadow:4px 6px 14px rgba(0,0,0,.28)}
.photo{position:absolute}
.band{position:absolute;top:0;right:13px;width:26px;height:100%;background:var(--plum-soft)}
.panel{position:absolute;top:0;right:0;width:38px;height:100%;background:var(--plum)}
.brand{position:absolute;display:flex;align-items:center;gap:2px}
.brand i{display:block;width:6px;height:6px;background:var(--plum)}
.brand b{font-family:"Playfair Display SC",Georgia,serif;font-weight:400;font-size:7px;letter-spacing:.5px;color:var(--plum)}
.brand.light i{background:#fff}
.brand.light b{color:#fff}
.title{position:absolute;font-family:"Playfair Display SC",Georgia,serif;font-weight:400;color:var(--forest);font-size:14px;line-height:1.15;letter-spacing:.3px;white-space:nowrap}
.title.plum{color:var(--plum)}
.title.white{color:#fff}
.copy{position:absolute;font-size:5.2px;line-height:1.45;color:var(--forest);text-align:justify}
.copy p+p{margin-top:4px}
.footer{position:absolute;bottom:4px;right:14px;font-size:2.8px;color:var(--muted);letter-spacing:.2px;white-space:nowrap}
.timeline-label{position:absolute;font-size:3.4px;font-weight:700;color:var(--ink);line-height:1.2}
.step{position:absolute;font-size:6px;font-weight:700;color:var(--ink)}
.benefits{position:absolute;left:18px;top:44px;width:277px;border-collapse:collapse;font-size:4px;color:var(--plum)}
.benefits th{background:var(--forest);color:#fff;font-weight:700;height:24px;font-size:3.4px;letter-spacing:.4px}
.benefits th.lead{font-family:"Playfair Display SC",Georgia,serif;font-size:4.6px;letter-spacing:1px;text-align:center}
.benefits td{padding:1.6px 3px;line-height:1.2}
.benefits td.tick{text-align:center;color:var(--tick);width:42px}
.fee-list{position:absolute;left:22px;top:52px;width:150px;list-style:none;font-size:4.6px;color:var(--forest);line-height:1.35}
.fee-list>li{font-weight:700;padding-left:6px;position:relative}
.fee-list>li::before{content:"›";position:absolute;left:0}
.fee-list span{display:block;font-weight:400;padding-left:6px;color:var(--ink)}
.legend{position:absolute;font-size:3.4px;color:var(--plum);display:grid;grid-template-columns:60px 50px;row-gap:1px}
.legend i{display:inline-block;width:3px;height:3px;margin-right:2px;vertical-align:middle}
</style>
</head>
<body>

<section class="slide" style="left:107px;top:21px">
  <div class="photo" role="img" aria-label="Lakeside temple with tiered pagoda roofs, misty mountains and flowers" style="inset:0;background:linear-gradient(180deg,#7d8493 0%,#a6adb6 35%,#4d5f55 62%,#5b7f78 80%,#4a6c68 100%)"></div>
  <div class="band"></div>
  <div class="brand light" style="right:14px;top:30px"><i></i><b>KCC</b></div>
  <h1 class="title white" style="right:46px;top:32px;font-size:12.5px;text-align:right">Kestrel Capital Circle</h1>
  <p style="position:absolute;right:46px;top:52px;font-family:'Playfair Display SC',serif;font-size:4.6px;color:#fff">Invest in Bali | Live in Paradise | Join the Circle</p>
  <p style="position:absolute;right:46px;top:61px;font-family:'Playfair Display SC',serif;font-size:3.8px;letter-spacing:1.3px;color:#fff">Investment Prospectus | August 2020</p>
</section>

<section class="slide" style="left:474px;top:21px">
  <div class="photo" role="img" aria-label="Sunset sky with glowing clouds over a calm sea" style="inset:0;background:linear-gradient(180deg,#e39459 0%,#f1b27a 28%,#c48a88 55%,#9c6c7a 72%,#b88476 88%,#a76f6e 100%)"></div>
  <div class="band"></div>
  <div class="brand light" style="right:14px;top:36px"><i></i><b>KCC</b></div>
  <h2 class="title plum" style="right:52px;top:33px;font-size:15px;text-align:right;line-height:1.6">Welcome<br>KCC Overview</h2>
</section>

<section class="slide" style="left:107px;top:214px">
  <h2 class="title" style="left:15px;top:38px;font-size:13.5px"><span style="color:var(--mauve)">The World</span><br>is Changing</h2>
  <div class="copy" style="left:15px;top:80px;width:137px;font-size:5.6px">“The world is undergoing a great transformational change; new ideas, beliefs, and concepts are required for humanity to shift to the next stage of evolution, with a focus on shared values of planetary sustainability, business integrity, and loving compassion for all living things.”</div>
  <p style="position:absolute;right:161px;top:143px;font-family:'Playfair Display SC',serif;font-size:5.4px;color:var(--plum)">Kestrel Capital Circle</p>
  <div class="photo" role="img" aria-label="Temple pagoda reflected in still lake water" style="left:168px;top:0;width:107px;height:175px;background:linear-gradient(180deg,#e9e1d8 0%,#c6bfb2 35%,#3f4a40 55%,#7d7c73 75%,#b2b0a6 100%)"></div>
  <div class="panel"></div>
  <div class="brand light" style="right:8px;top:42px"><i></i><b>KCC</b></div>
  <p class="footer" style="right:160px">Kestrel Capital Circle Presentation | Meridian Holdings Group | Page 3</p>
</section>

<section class="slide" style="left:474px;top:214px">
  <div class="photo" role="img" aria-label="Woven lanterns above a beach at sunset with sun loungers" style="left:0;top:0;width:118px;height:175px;background:linear-gradient(180deg,#8c7aa0 0%,#d8906a 35%,#e6a27b 50%,#8b7a75 72%,#4d5b3c 100%)"></div>
  <div class="brand" style="right:14px;top:18px"><i></i><b>KCC</b></div>
  <h2 class="title" style="right:18px;top:47px;font-size:14px;text-align:right">What is Kestrel<br>Capital Circle?</h2>
  <div class="copy" style="left:138px;top:89px;width:157px">
    <p><b>Kestrel Capital Circle (KCC)</b> is a social club of conscious investors, influencers and entrepreneurs creating the New Paradigm.</p>
    <p>Our mission is to support profitable impact-driven projects, improve the lives of our members and the local community, and foster greater sustainability on the island of Bali.</p>
  </div>
  <p class="footer">Kestrel Capital Circle Presentation | Meridian Holdings Group | Page 4</p>
</section>

<section class="slide" style="left:107px;top:408px">
  <div class="photo" role="img" aria-label="Carved stone deity statue among tropical foliage" style="left:24px;top:34px;width:111px;height:141px;background:linear-gradient(160deg,#3f5a32 0%,#a49f86 40%,#8c8670 70%,#5d5540 100%)"></div>
  <div class="brand" style="right:17px;top:17px"><i></i><b>KCC</b></div>
  <h2 class="title" style="left:149px;top:32px">The New<br>Paradigm</h2>
  <div class="copy" style="left:149px;top:73px;width:142px;font-size:5px">
    <p>A <b>paradigm</b> is generally defined as a framework that has unwritten rules and that directs actions. A <b>shift</b> occurs when one <b>paradigm</b> loses its influence and another takes over. We are witnessing the collapse of the old paradigm; a system built on scarcity, lack, and fear. Hence, we sit on the precipice of a <b>New Paradigm</b> -- a loving, supportive, and collaborative framework that provides abundance for everyone.</p>
    <p>Bali is the epicenter for emerging ideas; it is a hub for new networks, systems, communities, and projects that redefine the way we relate to each other and the world.</p>
  </div>
  <p class="footer">Kestrel Capital Circle Presentation | Meridian Holdings Group | Page 5</p>
</section>

<section class="slide" style="left:474px;top:408px">
  <div class="photo" role="img" aria-label="Water garden with stepping stones, stone statues and a tiered fountain" style="left:0;top:0;width:313px;height:116px;background:linear-gradient(180deg,#a9b1ad 0%,#5f7250 40%,#6e7a6c 65%,#3e514a 100%)"></div>
  <div class="brand light" style="right:14px;top:14px"><i></i><b>KCC</b></div>
  <h2 class="title white" style="right:17px;top:73px;text-align:right;font-size:15px">Our<br>Core Values</h2>
  <p style="position:absolute;left:0;width:313px;top:123px;text-align:center;font-family:'Playfair Display SC',serif;font-weight:700;font-size:7px;color:var(--plum)">People, Planet, Profit Truth, Trust, Faith.</p>
  <p class="copy" style="left:24px;top:136px;width:265px;text-align:center;font-size:5px">KCC invests in initiatives that are beneficial for the people, the planet, and profits; this means that every stakeholder is considered. Stakeholders are its members, partners, employees, and the planet. Impact is what drives our members, while profits are what sustains them.</p>
  <p class="footer">Kestrel Capital Circle Presentation | Meridian Holdings Group | Page 6</p>
</section>

<section class="slide" style="left:107px;top:601px">
  <h2 class="title" style="left:15px;top:15px">Why Bali?</h2>
  <p style="position:absolute;left:15px;top:42px;font-size:7px;color:var(--forest)">Asked from a different perspective, <b>WHY NOT</b> Bali?</p>
  <div class="copy" style="left:17px;top:58px;width:172px;text-align:left;font-size:5.3px;line-height:1.35">
    <p>Bali offers Western country nationals an extremely low cost of living and an amazing quality of life. For example, Canggu is rated as a top 5 digital nomad destination in the world. Benefits of living on the “Island of the Gods” include affordability, friendly locals, low crime, great weather, and access to nature and healthy living. A number of expats have moved to Bali to experience life in paradise in recent years.</p>
    <p>Moreover, with increased border control and immigration restrictions resulting from COVID-19, as well as the challenging impact that the virus has had on the lifestyle of people in Western countries, gaining a work and residency permit for Bali has become more desirable. There has been little impact from COVID-19 in Bali compared to other geographies, which makes it even more attractive as a destination.</p>
  </div>
  <div class="photo" role="img" aria-label="Volcano at dusk under a pink and violet sky above green rice terraces" style="left:196px;top:44px;width:135px;height:135px;border-radius:50%;background:linear-gradient(180deg,#c3608f 0%,#8b5ea0 35%,#4e3a6c 55%,#3b4f2c 78%,#5c7a36 100%)"></div>
  <p class="footer" style="right:160px">Kestrel Capital Circle Presentation | Meridian Holdings Group | Page 7</p>
</section>

<section class="slide" style="left:472px;top:601px">
  <div class="photo" role="img" aria-label="Waterfalls cascading down a lush green cliff" style="left:0;top:0;width:60px;height:175px;background:linear-gradient(90deg,#24311f 0%,#5a6c47 40%,#c7cdc2 50%,#3c4c2f 70%,#2c3a24 100%)"></div>
  <div class="brand" style="right:14px;top:16px"><i></i><b>KCC</b></div>
  <h2 class="title" style="left:73px;top:15px">What is a KITAS?</h2>
  <div class="copy" style="left:73px;top:46px;width:223px;font-size:4.5px;line-height:1.5;color:var(--ink)">
    <p>A <b>KITAS (<i>Kartu Izin Tinggal Sementara</i>, or Temporary Stay Permit Card)</b> is an Indonesian government permit that allows foreign nationals to stay for a specified period of time without having to renew their visas and/or work in Indonesia. When border restrictions are enforced, it is the only way for a foreigner to enter the country.</p>
    <p style="text-align:left">There are <b>two</b> ways to obtain a KITAS:<br>&nbsp;&nbsp;1. Company Sponsorship: an existing business in Bali employs and sponsors a person<br>&nbsp;&nbsp;2. Investor KITAS: invest $175,000+ into a foreign-owned local entity (PT PMA) and receive an Investor KITAS for two years, with the option to extend</p>
    <p style="font-weight:700;color:var(--forest)">The Kestrel Capital Circle offers an alternative.</p>
    <p>Among other benefits mentioned previously, the KCC membership will include a 2-year commissioner KITAS, with the option to extend. While this option does require a capital investment, it is considerably less than USD $175,000 and requires zero knowledge, experience and motivation to manage a business in Bali; supports local people and the land; provides a potential return on Investment; and gives positive ROI on impact driven investments.</p>
  </div>
  <p class="footer">Kestrel Capital Circle Presentation | Meridian Holdings Group | Page 8</p>
</section>

<section class="slide" style="left:105px;top:795px">
  <div class="photo" role="img" aria-label="Turquoise waves breaking against a rocky tropical coastline under palm fronds" style="inset:0;background:linear-gradient(180deg,#7aa2c8 0%,#b7cde0 25%,#6c6a43 38%,#2a8fb2 55%,#8fd6e0 75%,#e6f4f5 100%)"></div>
  <div class="band"></div>
  <div class="brand light" style="right:14px;top:38px"><i></i><b>KCC</b></div>
  <h2 class="title plum" style="right:52px;top:30px;text-align:right;font-size:15px">Becoming<br>a Member</h2>
</section>

<section class="slide" style="left:472px;top:795px">
  <div class="brand" style="right:14px;top:16px"><i></i><b>KCC</b></div>
  <h2 class="title plum" style="left:22px;top:15px">Becoming a Member</h2>
  <p class="copy" style="left:26px;top:53px;width:256px;text-align:left;font-size:4.5px;color:var(--ink)">KCC invites a limited number of members to join the circle each month, and is selective based on a number of factors. There is a USD $1,000 deposit which is refunded to unsuccessful applicants. Remainder payment of USD $24,000* must be made within 48 hours of approval.</p>
  <div class="timeline-label" style="left:29px;top:81px">Submit Application and<br>$1,000 Deposit</div>
  <div class="timeline-label" style="left:109px;top:81px">Receive Invitation to Join</div>
  <div class="timeline-label" style="left:190px;top:81px">Receive Membership ID<br>&amp; Legal Documents</div>
  <div class="timeline-label" style="left:262px;top:81px">Open Circle<br>Bank Account</div>
  <svg style="position:absolute;left:0;top:0" width="313" height="175" viewBox="0 0 313 175">
    <line x1="30" y1="95" x2="30" y2="101" stroke="var(--deep-green)" stroke-width=".6"/>
    <line x1="110" y1="95" x2="110" y2="101" stroke="var(--teal)" stroke-width=".6"/>
    <line x1="190" y1="95" x2="190" y2="101" stroke="var(--magenta)" stroke-width=".6"/>
    <line x1="270" y1="95" x2="270" y2="101" stroke="var(--plum)" stroke-width=".6"/>
    <line x1="70" y1="103" x2="70" y2="110" stroke="var(--deep-green)" stroke-width=".6"/>
    <line x1="150" y1="103" x2="150" y2="110" stroke="var(--pink)" stroke-width=".6"/>
    <line x1="230" y1="103" x2="230" y2="110" stroke="var(--plum)" stroke-width=".6"/>
    <rect x="30" y="100" width="40" height="4" fill="var(--deep-green)"/>
    <rect x="70" y="100" width="40" height="4" fill="var(--forest)"/>
    <rect x="110" y="100" width="40" height="4" fill="var(--teal)"/>
    <rect x="150" y="100" width="40" height="4" fill="var(--pink)"/>
    <rect x="190" y="100" width="40" height="4" fill="var(--magenta)"/>
    <rect x="230" y="100" width="40" height="4" fill="var(--plum)"/>
    <circle cx="30" cy="95" r="1.3" fill="var(--deep-green)"/>
    <circle cx="110" cy="95" r="1.3" fill="var(--teal)"/>
    <circle cx="190" cy="95" r="1.3" fill="var(--magenta)"/>
    <circle cx="270" cy="95" r="1.3" fill="var(--plum)"/>
    <circle cx="70" cy="110" r="1.3" fill="var(--deep-green)"/>
    <circle cx="150" cy="110" r="1.3" fill="var(--pink)"/>
    <circle cx="230" cy="110" r="1.3" fill="var(--plum)"/>
  </svg>
  <span class="step" style="left:62px;top:90px">Step 2</span>
  <span class="step" style="left:142px;top:90px">Step 4</span>
  <span class="step" style="left:222px;top:90px">Step 6</span>
  <span class="step" style="left:22px;top:108px">Step 1</span>
  <span class="step" style="left:102px;top:108px">Step 3</span>
  <span class="step" style="left:182px;top:108px">Step 5</span>
  <span class="step" style="left:258px;top:108px">Step 7</span>
  <div class="timeline-label" style="left:69px;top:117px">Interview with KCC<br>Founder</div>
  <div class="timeline-label" style="left:149px;top:117px">Sign Membership<br>Agreement &amp; Make<br>Balance Payment<br><span style="font-weight:400;color:#777;display:block;margin-top:5px">Must be completed within<br>48 hours of approval</span></div>
  <div class="timeline-label" style="left:229px;top:117px">Begin KITAS<br>Processing<br><span style="font-weight:400;color:#777;display:block;margin-top:4px">This process may<br>take up to 2-3<br>months to<br>complete</span></div>
  <p style="position:absolute;left:72px;top:164px;font-size:2.6px;font-style:italic;color:var(--plum);white-space:nowrap">*$29,000 membership fee as a tax-deductible donation for US/UK citizens. $5,000 discount for existing KITAS holders</p>
  <p class="footer" style="bottom:2px">Kestrel Capital Circle Presentation | Meridian Holdings Group | Page 10</p>
</section>

<section class="slide" style="left:105px;top:989px">
  <h2 class="title plum" style="left:21px;top:15px">Member Benefits</h2>
  <div class="brand" style="right:16px;top:18px"><i></i><b>KCC</b></div>
  <table class="benefits">
    <tr><th class="lead">Example based on USD $25,000 investment</th><th>OPTION A<br>INVESTMENT CIRCLE<br><i style="font-weight:400">( EG. LHE PROJECT)</i></th><th>OPTION B<br>BUSINESS CIRCLE</th></tr>
    <tr><td style="font-style:italic">100 shares in (LHE) PT Lontar Harvest Estates (ROI $115,106)*</td><td class="tick">✓</td><td class="tick"></td></tr>
    <tr><td style="font-style:italic">Proceeds from the sales of product from a personal vanilla farm with 500 plants (ROI $56,687)*</td><td class="tick">✓</td><td class="tick"></td></tr>
    <tr><td>USD $10,000 in a bank account for investment into existing or new project</td><td class="tick"></td><td class="tick">✓</td></tr>
    <tr><td>A two-year KITAS work visa, with the option to extend</td><td class="tick">✓</td><td class="tick">✓</td></tr>
    <tr><td>Access to exclusive networking events and investment opportunities</td><td class="tick">✓</td><td class="tick">✓</td></tr>
    <tr><td>First right of refusal on new investment opportunities</td><td class="tick">✓</td><td class="tick">✓</td></tr>
    <tr><td>Access to professional business services; finance, legal, accounting and tax advice to minimise tax and maximise returns</td><td class="tick">✓</td><td class="tick">✓</td></tr>
    <tr><td>Access to support for migration: travel, accommodation and recommendations (restaurants, activities, wellness facilities, etc.)</td><td class="tick">✓</td><td class="tick">✓</td></tr>
    <tr><td>Opportunity to become a founding member and earn 6 figures</td><td class="tick">✓</td><td class="tick">✓</td></tr>
  </table>
  <p style="position:absolute;left:21px;top:162px;font-size:2.8px;color:var(--plum)">*Projected over 15 years</p>
  <p class="footer">Kestrel Capital Circle Presentation | Meridian Holdings Group | Page 11</p>
</section>

<section class="slide" style="left:472px;top:989px">
  <h2 class="title plum" style="left:21px;top:15px">Membership Fee Breakdown</h2>
  <div class="brand" style="right:14px;top:18px"><i></i><b>KCC</b></div>
  <p style="position:absolute;left:21px;top:41px;font-size:4.8px;color:var(--forest)">Based on a USD $25,000 investment, we allocate the following:</p>
  <ul class="fee-list">
    <li>Personal KCC Business Account (USD $10,000):<span>◦ Freedom of making investments within KCC ventures portfolio and/or individual business activities</span></li>
    <li>Circle Costs (USD $8,250):<span>◦ Operations, membership services, KITAS</span></li>
    <li>Programs (USD $3,000):<span>◦ Vocational and charitable assistance programs to aid the local Balinese communities</span></li>
    <li>Circle Investment Capital (USD $2,500):<span>◦ Capital for Founding Members to invest</span></li>
    <li>Circle Cash Reserves (USD $1,250):<span>◦ Cash flow is king. The circle keeps cash on reserve for miscellaneous expenses</span></li>
  </ul>
  <svg style="position:absolute;left:178px;top:42px" width="100" height="100" viewBox="0 0 100 100">
    <g transform="rotate(-90 50 50)" fill="none" stroke-width="9">
      <circle cx="50" cy="50" r="40" stroke="var(--teal)" stroke-dasharray="100.5 250" stroke-dashoffset="0"/>
      <circle cx="50" cy="50" r="40" stroke="var(--deep-green)" stroke-dasharray="12.6 250" stroke-dashoffset="-100.5"/>
      <circle cx="50" cy="50" r="40" stroke="var(--plum)" stroke-dasharray="82.9 250" stroke-dashoffset="-113.1"/>
      <circle cx="50" cy="50" r="40" stroke="var(--magenta)" stroke-dasharray="15 250" stroke-dashoffset="-196"/>
      <circle cx="50" cy="50" r="40" stroke="var(--pink)" stroke-dasharray="25 250" stroke-dashoffset="-211"/>
      <circle cx="50" cy="50" r="40" stroke="var(--mint)" stroke-dasharray="15.3 250" stroke-dashoffset="-236"/>
    </g>
  </svg>
  <div class="legend" style="left:182px;top:145px">
    <span><i style="background:var(--teal)"></i>Investment</span><span><i style="background:var(--deep-green)"></i>Charity</span>
    <span><i style="background:var(--plum)"></i>Administrative Expenses</span><span><i style="background:var(--magenta)"></i>Vocation Program</span>
    <span><i style="background:var(--pink)"></i>CIC</span><span><i style="background:var(--mint)"></i>Cash Reserves</span>
  </div>
  <p style="position:absolute;left:21px;top:158px;font-size:2.8px;font-style:italic;color:var(--plum)">*$5,000 discount for KITAS holders</p>
  <p class="footer">Kestrel Capital Circle Presentation | Meridian Holdings Group | Page 12</p>
</section>

</body>
</html>
```